Sparrowgate Petals Website v.1 - attract floral shop franchisees

I need a simple information website for my new business. We are a franchisor of flower shops. The overall purpose of the website is to promote the company and the service, especially to potential franchisees and retailers. Only about 4 pages are required including homepage, About, For Supermarkets, For Franchisees, and Contact. No special functions are required except the site will have two separate inquiry forms that must be filled out online and submitted via automated email. Similarly, an email form should be linked from the Contact page. I have a logo and business cards designed by ArtQuarry, and I would like the site to have a consistent color scheme and style. The key to design will be to express the joy and love associated with flowers and floral bouquets.
IMPORTANT - I will be exporting the website design to Wordpress CMS in a site hosted by HostNimbus. For smooth integration into WordPress hosted by HostNimbus, the designer should build the site using a WordPress-friendly format. Ideally, they should use HTML, CSS, and PHP. Creating a custom theme or using a page builder that exports to WordPress-compatible files is best. This ensures the site can be easily imported and managed within WordPress.

Target Market(s)

Potential franchisees (existing florists or creative types who might like to own a floral business) and supermarkets who might want us to run their floral department

Industry/Entity Type

Floral retailing

Requirements
Must have
• A brand theme that is beautiful, consistent throughout and builds on the logo design
Nice to have
• Show gender and ethnic diversity in customers and florists. Pictures of happy florists (for franchisees) and pictures of amazing floral department displays (for supermarkets)

```html
<!DOCTYPE html>
<html lang="en">
<head>
<meta charset="utf-8">
<title>Sparrowgate Petals</title>
<link href="https://fonts.googleapis.com/css2?family=Pinyon+Script&family=Poppins:wght@300;400;500&display=swap" rel="stylesheet">
<style>
:root{
  --orange:#f2ad2b;
  --orange-deep:#eda526;
  --green:#2f9e5c;
  --green-dark:#23894c;
  --ink:#1f1f1f;
  --text:#6b6b6b;
  --hero-bg:#faf5f5;
  --soft-bg:#fbf9f9;
  --card-bg:#f3f3f3;
  --white:#ffffff;
}
*{margin:0;padding:0;box-sizing:border-box}
html,body{width:1200px;height:3518px;overflow:hidden}
body{position:relative;background:var(--white);font-family:"Poppins",sans-serif;color:var(--text)}
.abs{position:absolute}
.script{font-family:"Pinyon Script",cursive;color:var(--ink);font-weight:400;line-height:1}
.pill{position:absolute;display:flex;align-items:center;justify-content:center;border-radius:30px;background:var(--orange);color:var(--ink);font-size:13px;letter-spacing:3px;font-weight:500;text-transform:uppercase}

.page-bg{left:0;top:0;width:1200px;height:2266px;background:var(--soft-bg)}
.hero-bg{left:0;top:0;width:1200px;height:720px;background:var(--hero-bg)}
.texture-bg{left:0;top:720px;width:1200px;height:1546px;background:linear-gradient(180deg,#f6f4f4 0%,#f8f3f3 45%,#f5f2f2 100%)}

/* header */
.brand{left:27px;top:50px;display:flex;align-items:center;gap:10px;font-size:18px;font-weight:500;color:var(--orange)}
.brand-dot{width:26px;height:26px;border-radius:50%;background:var(--green)}
.nav a{position:absolute;top:57px;font-size:13px;letter-spacing:3px;color:var(--ink);text-decoration:none;font-weight:500}
.nav-contact{left:992px;top:45px;width:152px;height:40px}

/* hero */
.hero-title{left:78px;top:228px;font-size:62px}
.hero-text{left:78px;top:302px;width:460px;font-size:12.5px;line-height:19.5px;font-weight:300}
.hero-btn{left:78px;top:430px;width:140px;height:38px}
.hero-photo{left:587px;top:123px;width:613px;height:587px;background:radial-gradient(ellipse at 55% 45%,#f8d5dd 0%,#f7e6e6 45%,rgba(250,245,245,0) 75%)}

/* waves */
.wave{left:0;width:1200px}

/* hex photos */
.hex-frame{}
.hex-photo{clip-path:polygon(50% 0,100% 25%,100% 75%,50% 100%,0 75%,0 25%)}
.hex-about{left:91px;top:962px;width:370px;height:423px;background:linear-gradient(160deg,#7a5a48 0%,#e56f86 40%,#c9405d 65%,#3d4a2e 100%)}
.hex-frostlyn{left:739px;top:1598px;width:368px;height:422px;background:linear-gradient(150deg,#e9e4de 0%,#d8a53a 35%,#7b4a24 65%,#262626 100%)}

.deco{background:radial-gradient(circle,rgba(47,158,92,.35) 0%,rgba(47,158,92,0) 70%)}

/* about */
.about-title{left:570px;top:935px;font-size:50px}
.about-text{left:566px;top:1008px;width:552px;font-size:12.5px;line-height:20.1px;font-weight:300}
.about-text p+p{margin-top:20px}
.about-btn{left:568px;top:1380px;width:151px;height:40px}

/* frostlyn */
.frost-title{left:98px;top:1625px;font-size:54px}
.frost-text{left:97px;top:1698px;width:545px;font-size:16.5px;line-height:25.7px;font-weight:300}
.frost-badge{left:110px;top:1914px;width:76px;height:75px;background:#e4dfdc}

/* cards */
.card{position:absolute;top:2501px;width:476px;height:256px;background:var(--card-bg)}
.card-supermarkets{left:108px}
.card-franchise{left:635px}
.card h2{position:absolute;left:38px;top:28px;font-size:46px}
.card p{position:absolute;left:37px;top:96px;width:410px;font-size:14.5px;line-height:22.5px;font-weight:300}
.card .pill{left:38px;top:185px;width:152px;height:40px}

/* footer */
.footer{left:0;top:2942px;width:1200px;height:576px;background:var(--orange)}
.foot-title{font-size:46px}
.foot-links a{position:absolute;left:102px;font-size:14px;letter-spacing:3.5px;color:var(--ink);text-decoration:none;font-weight:500}
.contact-icon{width:40px;height:40px;border:2px solid var(--green);border-radius:50%;display:flex;align-items:center;justify-content:center}
.contact-line{font-size:15px;color:var(--ink)}
.newsletter{left:678px;top:3104px;width:458px;height:280px;background:var(--white)}
.newsletter h3{position:absolute;left:45px;top:30px;font-size:46px}
.email-field{position:absolute;left:26px;top:113px;width:286px;height:53px;border:1.5px solid #555;border-radius:30px;padding-left:36px;display:flex;align-items:center;font-size:15px;color:#777}
.subscribe{position:absolute;left:26px;top:188px;width:286px;height:52px;border-radius:30px;background:var(--green);color:var(--white);display:flex;align-items:center;justify-content:center;font-size:16px;letter-spacing:4px}
.news-photo{position:absolute;left:318px;top:63px;width:140px;height:217px;background:linear-gradient(170deg,#fff 0%,#f1c5cf 35%,#cfe0dc 70%,#e9dccb 100%)}
.copyright{left:0;top:3472px;width:1200px;text-align:center;font-size:15px;color:var(--ink)}
</style>
</head>
<body>
<div class="abs page-bg"></div>
<div class="abs hero-bg"></div>
<div class="abs texture-bg" role="img" aria-label="Faint background photo of a floral arrangement"></div>
<div class="abs hero-photo" role="img" aria-label="Pink gerbera daisies and white blooms in a speckled enamel pot"></div>

<header>
  <div class="abs brand"><span class="brand-dot"></span>Sparrowgate Petals</div>
  <nav class="nav">
    <a style="left:276px" href="#">HOME</a>
    <a style="left:373px" href="#">ABOUT</a>
    <a style="left:485px" href="#">FOR SUPERMARKETS</a>
    <a style="left:733px" href="#">FOR FRANCHISEES</a>
  </nav>
  <a class="pill nav-contact" href="#">Contact</a>
</header>

<section class="hero">
  <h1 class="abs script hero-title">Sparrowgate Petals</h1>
  <p class="abs hero-text">Fresh flowers convey beauty and love, and in our view should become something every person regularly enjoys.&nbsp; Sparrowgate Petals is an entrepreneurial company created to make top quality fresh flowers and professionally-designed bouquets accessible to every consumer at affordable prices.</p>
  <div class="pill hero-btn">Contact</div>
</section>

<svg class="abs wave" style="top:587px;height:218px" viewBox="0 430 879 160" preserveAspectRatio="none">
  <path fill="#f2ad2b" d="M0,437 C150,420 300,470 450,508 C600,545 760,528 879,512 C760,540 600,562 450,522 C300,488 150,488 0,506 Z"/>
  <path fill="#2f9e5c" d="M0,510 C150,488 330,505 432,543 C300,530 120,545 0,585 Z"/>
</svg>

<section class="about">
  <div class="abs deco" style="left:80px;top:810px;width:90px;height:180px" role="img" aria-label="Small illustrated bee with a dashed looping flight path"></div>
  <svg class="abs" style="left:72px;top:939px" width="408" height="470" viewBox="0 0 408 470">
    <polygon points="204,2 406,118 406,352 204,468 2,352 2,118" fill="none" stroke="#2f9e5c" stroke-width="2.5" stroke-dasharray="9 7"/>
  </svg>
  <div class="abs hex-photo hex-about" role="img" aria-label="Shop display of pink roses and mixed bouquets by a window"></div>
  <h2 class="abs script about-title">About</h2>
  <div class="abs about-text">
    <p>Professional florists typically sell the finest quality stems, design the most beautiful bouquets and provide the finest customer service, but their costs – of floral products, retail spaces, labor and marketing – force them to pass high prices along to customers.&nbsp; Supermarket flower departments benefit from high customer footfall, economies of scale and low pricing, but their quality of stems and bouquets is typically poor, staffing is limited, and staff turnover is high which can result in inefficiency, wastage, poorly merchandised selections and limited service.</p>
    <p>Sparrowgate Petals brings the best of professional florists and supermarkets together for the benefit of consumers.&nbsp; It supports a national network of owner-operator franchisees, who in many cases are multi-site professional florists, with comprehensive services to enhance franchise profitability.&nbsp; Sparrowgate Petals works with some of the country’s largest and most progressive supermarkets to provide franchisee ownership and operation of their strategically important floral departments.&nbsp; Supermarkets find that Sparrowgate Petals is able to improve their financial outcomes, provide attentive customer service and satisfaction, and lift the quality of the entire store environment.</p>
  </div>
  <div class="pill about-btn">Contact</div>
</section>

<section class="frostlyn">
  <div class="abs deco" style="left:1044px;top:1451px;width:80px;height:180px" role="img" aria-label="Small illustrated bee with a dashed looping flight path"></div>
  <svg class="abs" style="left:719px;top:1574px" width="410" height="470" viewBox="0 0 410 470">
    <polygon points="205,2 408,118 408,352 205,468 2,352 2,118" fill="none" stroke="#2f9e5c" stroke-width="2.5" stroke-dasharray="9 7"/>
  </svg>
  <div class="abs hex-photo hex-frostlyn" role="img" aria-label="Fruit skewer tower beside a chocolate fountain"></div>
  <h2 class="abs script frost-title">Frostlyn</h2>
  <p class="abs frost-text">Sparrowgate Petals operates in partnership with Frostlyn Group, the leading franchisor of sushi stations and pre-packaged fruit &amp; vegetable departments to supermarkets across the United States and United Kingdom.&nbsp; Sparrowgate Petals’ combination of floral and supermarket franchising expertise guarantees that consumers, franchisees and supermarket partners each receive exceptional service and value.</p>
  <div class="abs frost-badge" role="img" aria-label="Partner badge"></div>
</section>

<svg class="abs wave" style="top:2125px;height:210px" viewBox="0 1556 879 154" preserveAspectRatio="none">
  <path fill="#f2ad2b" d="M0,1636 C250,1655 500,1580 879,1560 L879,1622 C650,1622 450,1640 330,1660 C200,1678 80,1660 0,1642 Z"/>
  <path fill="#2f9e5c" d="M450,1668 C600,1632 760,1618 879,1626 L879,1707 C800,1660 640,1648 450,1668 Z"/>
</svg>

<section class="services">
  <div class="abs deco" style="left:30px;top:2426px;width:80px;height:182px" role="img" aria-label="Small illustrated bee with a dashed looping flight path"></div>
  <div class="abs deco" style="left:1106px;top:2434px;width:80px;height:180px" role="img" aria-label="Small illustrated bee with a dashed looping flight path"></div>
  <article class="card card-supermarkets">
    <h2 class="script">For Supermarkets</h2>
    <p>Supermarket flower departments benefit from high customer footfall, economies of scale and low pricing. However their quality of stems and bouquets is ...</p>
    <div class="pill">Read More</div>
  </article>
  <article class="card card-franchise">
    <h2 class="script">For Franchisee</h2>
    <p>Sparrowgate Petals supports a national network of owner-operator franchisees with comprehensive services to enhance franchise profits.</p>
    <div class="pill">Read More</div>
  </article>
</section>

<footer>
  <div class="abs footer" role="img" aria-label="Warm orange band with a faint floral texture"></div>
  <h3 class="abs script foot-title" style="left:78px;top:3108px">About</h3>
  <nav class="foot-links">
    <a style="top:3203px" href="#">HOME</a>
    <a style="top:3252px" href="#">ABOUT</a>
    <a style="top:3300px" href="#">FOR SUPERMARKETS</a>
    <a style="top:3349px" href="#">FOR FRANCHISEE</a>
    <a style="top:3399px" href="#">CONTACT</a>
  </nav>
  <h3 class="abs script foot-title" style="left:369px;top:3108px">Contact</h3>
  <div class="abs contact-icon" style="left:363px;top:3196px">
    <svg width="18" height="18" viewBox="0 0 24 24"><path fill="#2f9e5c" d="M6.6 10.8a15.1 15.1 0 0 0 6.6 6.6l2.2-2.2c.3-.3.7-.4 1-.2 1.1.4 2.3.6 3.6.6.6 0 1 .4 1 1V20c0 .6-.4 1-1 1A17 17 0 0 1 3 4c0-.6.4-1 1-1h3.5c.6 0 1 .4 1 1 0 1.3.2 2.5.6 3.6.1.3 0 .7-.2 1z"/></svg>
  </div>
  <div class="abs contact-line" style="left:420px;top:3205px">+1 555 014 2287</div>
  <div class="abs contact-icon" style="left:363px;top:3256px">
    <svg width="18" height="18" viewBox="0 0 24 24"><path fill="#2f9e5c" d="M3 6h18v12H3z"/><path fill="none" stroke="#f2ad2b" stroke-width="1.6" d="M3 6l9 7 9-7"/></svg>
  </div>
  <div class="abs contact-line" style="left:420px;top:3265px">info@sparrowgate-petals.com</div>
  <div class="abs newsletter">
    <h3 class="script">Newsletter</h3>
    <div class="email-field">Email Address</div>
    <div class="subscribe">SUBSCRIBE NOW</div>
    <div class="news-photo" role="img" aria-label="Pink and white bouquet in a pale blue jug"></div>
  </div>
  <p class="abs copyright">Copyright 2024 Sparrowgate. All Rights Reserved.</p>
</footer>
</body>
</html>
```